Restaurant Facility Equipment & Store Maintenance/

I need a flyer showing commercial/industrial kitchen equipment photos we work on Hot Equipment & Cold Equipment and offer many services. see attached highlights

```html
<!DOCTYPE html>
<html lang="en">
<head>
<meta charset="utf-8">
<title>Restaurant Facility Equipment &amp; Store Maintenance</title>
<link rel="stylesheet" href="https://fonts.googleapis.com/css2?family=Bebas+Neue&family=Poppins:wght@400;600;700&display=swap">
<style>
  :root {
    --blue: #0f3ba8;
    --blue-dark: #0a2f8f;
    --yellow: #f7c400;
    --ink: #111827;
    --body: #2b3040;
    --white: #ffffff;
  }
  * { margin: 0; padding: 0; box-sizing: border-box; }
  html, body { width: 927px; height: 1200px; overflow: hidden; background: var(--white); }
  .flyer { position: relative; width: 927px; height: 1200px; overflow: hidden; background: var(--white); font-family: "Poppins", sans-serif; }

  .hero-photo {
    position: absolute; left: 0; top: 0; width: 927px; height: 480px;
    background: linear-gradient(160deg, #d9d5cf 0%, #b8b2aa 35%, #9c9085 60%, #b79a7d 85%, #c8a884 100%);
  }
  .hero-wave { position: absolute; left: 0; top: 0; width: 927px; height: 480px; }
  .side-band { position: absolute; left: 0; top: 0; width: 927px; height: 1200px; pointer-events: none; }

  .round-photo {
    position: absolute; width: 188px; height: 188px; border-radius: 50%;
    border: 9px solid var(--white);
    box-shadow: 0 0 0 1px #e3e6ee;
  }
  .round-photo.hood { left: 677px; top: 452px; background: radial-gradient(circle at 50% 45%, #f4f4f4 0%, #cfcfd0 55%, #8d8f93 100%); }
  .round-photo.range { left: 677px; top: 661px; background: linear-gradient(180deg, #e6e7ea 0%, #c4c6ca 50%, #8e9196 100%); }
  .round-photo.barista { left: 677px; top: 872px; background: linear-gradient(135deg, #b9b7b3 0%, #8d7a6b 50%, #5d4b40 100%); }

  .headline {
    position: absolute; left: 41px; top: 486px;
    font-family: "Bebas Neue", sans-serif; font-weight: 400; font-size: 30px; line-height: 30px;
    color: var(--blue); letter-spacing: -0.3px; white-space: nowrap;
    transform: scaleY(1.14); transform-origin: left top;
  }
  .intro {
    position: absolute; left: 41px; top: 560px; width: 625px;
    font-size: 16.4px; line-height: 22.8px; color: var(--body);
  }
  .intro strong { color: var(--ink); font-weight: 700; }

  .services-title {
    position: absolute; left: 41px; top: 688px;
    font-size: 23px; font-weight: 700; color: var(--blue); letter-spacing: 0.2px;
  }
  .service-list { position: absolute; left: 41px; top: 733px; width: 620px; list-style: none; }
  .service-list li {
    position: relative; padding-left: 32px; margin-bottom: 8.3px;
    font-size: 15px; font-weight: 600; line-height: 20.5px; color: var(--ink);
  }
  .tick { position: absolute; left: 0; top: 0; width: 22px; height: 22px; }

  .service-row { position: absolute; left: 41px; top: 1093px; display: flex; gap: 28px; list-style: none; }
  .service-row li { position: relative; padding-left: 32px; font-size: 15px; font-weight: 600; line-height: 22px; color: var(--ink); white-space: nowrap; }

  .closing {
    position: absolute; left: 0; top: 1130px; width: 927px; text-align: center;
    font-size: 15.6px; font-weight: 700; line-height: 23px; color: var(--blue);
  }
</style>
</head>
<body>
<svg width="0" height="0" style="position:absolute">
  <defs>
    <symbol id="tick" viewBox="0 0 24 24">
      <path d="M20.5 8.5 A9.5 9.5 0 1 1 16.5 4" fill="none" stroke="#0f3ba8" stroke-width="2" stroke-linecap="round"/>
      <path d="M7.5 11.5 L11.5 15.5 L21 5" fill="none" stroke="#0f3ba8" stroke-width="2.2" stroke-linecap="round" stroke-linejoin="round"/>
    </symbol>
  </defs>
</svg>

<main class="flyer">
  <div class="hero-photo" role="img" aria-label="Photo of a stainless steel commercial kitchen with stacked convection ovens, range, prep sinks and a reach-in refrigerator"></div>

  <svg class="hero-wave" viewBox="0 0 927 480" aria-hidden="true">
    <path d="M0 398 C120 448 260 470 400 464 C540 456 610 350 720 340 C810 332 880 360 927 382 L927 480 L0 480 Z" fill="#ffffff"/>
    <path d="M215 466 C330 474 420 462 470 438 C560 392 620 348 720 340 C810 334 880 362 927 384" fill="none" stroke="#f7c400" stroke-width="9"/>
    <path d="M0 398 C120 448 260 470 400 464 C540 456 610 350 720 340 C810 332 880 360 927 382" fill="none" stroke="#ffffff" stroke-width="5"/>
  </svg>

  <svg class="side-band" viewBox="0 0 927 1200" aria-hidden="true">
    <path d="M927 408 L868 408 C805 408 771 470 771 540 L771 1000 C771 1065 815 1106 878 1106 L927 1106 Z" fill="#0f3ba8"/>
  </svg>

  <div class="round-photo hood" role="img" aria-label="Photo of a bright commercial kitchen with a long stainless exhaust hood"></div>
  <div class="round-photo range" role="img" aria-label="Photo of a stainless cooking line with hanging utensils"></div>
  <div class="round-photo barista" role="img" aria-label="Photo of two workers servicing an espresso machine"></div>

  <h1 class="headline">INSTALLATION, REBUILDS, OSHA INSPECTION, AND PREVENTIVE<br>MAINTENANCE SERVICES FOR DENVER METRO AND SURROUNDING AREAS.</h1>

  <p class="intro"><strong>"We handle everything from the front door to the back door."</strong> We offer hot and cold equipment repair, cleaning, maintenance, handyman work, drywall, painting, door closers, floors, and ceiling tiles. For any need in your restaurant, call us and we will send a skilled technician to manage all your commercial and industrial facility requirements.</p>

  <h2 class="services-title">OUR SERVICES</h2>

  <ul class="service-list">
    <li><svg class="tick"><use href="#tick"/></svg>CKETA Certified Technicians</li>
    <li><svg class="tick"><use href="#tick"/></svg>Round-the-clock emergency services</li>
    <li><svg class="tick"><use href="#tick"/></svg>Customers who subscribe to preventive maintenance<br>services receive a reduced rate on hourly labor charges.</li>
    <li><svg class="tick"><use href="#tick"/></svg>Original equipment manufacturer (OEM) parts</li>
    <li><svg class="tick"><use href="#tick"/></svg>30-day warranty on all OEM parts installed</li>
    <li><svg class="tick"><use href="#tick"/></svg>Equipment Cleaning &amp; Rebuilds</li>
    <li><svg class="tick"><use href="#tick"/></svg>Used equipment available for purchase or rental</li>
    <li><svg class="tick"><use href="#tick"/></svg>Specialized Programs for Preventive Maintenance of Equipment</li>
    <li><svg class="tick"><use href="#tick"/></svg>Installation and Repair of Restaurant Equipment</li>
    <li><svg class="tick"><use href="#tick"/></svg>Repair or replace restaurant furniture</li>
    <li><svg class="tick"><use href="#tick"/></svg>Comprehensive licensed electrical contractor services for both<br>interior and exterior projects, including lighting system upgrades.</li>
  </ul>

  <ul class="service-row">
    <li><svg class="tick"><use href="#tick"/></svg>Building Graffiti Removal Services</li>
    <li><svg class="tick"><use href="#tick"/></svg>Hot &amp; Cold Equipment</li>
    <li><svg class="tick"><use href="#tick"/></svg>Food Service Trucks</li>
  </ul>

  <p class="closing">WE REPAIR FLOORS, WALLS, COUNTERS, DÉCOR, SIGNAGE, PARKING LOTS,<br>DUMPSTERS, AND MORE. IF YOU HAVE IT, WE PROBABLY FIX IT</p>
</main>
</body>
</html>
```